KTV Business Card

Create a Simple but Elegant business card for a Luxury Off Road Vehicle and Accessories sales Company. Center of Letters we usually fill with red or a carbon fiber we don't want to limit creativity so anything goes. I think we would prefer large logo on the front and a smaller logo with infused QR reader on the back.
Some Ideas to get you heading more in the right direction are to put them on a thicker cardstock with red edges and we would need our logo letter (KTV) filled in with red. Example is the Vantorelli card in our brief. For the side with our info on it we are looking for our logo to include an embedded QR reader also in our brief.
Information to include 2 bullet points: Luxury Off Road Vehicle Sales / Custom Off Road Bumpers
Address:518 Pelling Road, Suite 164, Halvern Springs, Calder
Phone# 555-318-0467,
Website: WWW.KTV-TRAILGEAR.EXAMPLE
Facebook: facebook.com/KTVTrailGear
Instagram: instagram.com/ktv_trailgear
Target Market(s)
Exotic Vehicle and Outdoor enthusiasts.
Industry/Entity Type
Business
Look and feel

```html
<!DOCTYPE html>
<html lang="en">
<head>
<meta charset="utf-8">
<title>KTV Business Card</title>
<link href="https://fonts.googleapis.com/css2?family=Oswald:wght@400;500&display=swap" rel="stylesheet">
<style>
  :root {
    --page: #ececec;
    --card-dark: #1c1a1a;
    --plate-deep: #1a0607;
    --plate-mid: #4a1214;
    --plate-glow: #6e1c1f;
    --brand-red: #7d1c20;
    --accent-red: #a3262b;
    --steel: #dfe3e6;
    --text-light: #f2f2f2;
    --divider: #5a2326;
  }
  * { margin: 0; padding: 0; box-sizing: border-box; }
  html, body { width: 974px; height: 1200px; overflow: hidden; }
  body {
    background: var(--page);
    font-family: "Oswald", "Arial Narrow", sans-serif;
    position: relative;
  }
  .card {
    position: absolute;
    left: 77px;
    width: 800px;
    height: 469px;
    overflow: hidden;
  }
  .card-front { top: 92px; }
  .card-back { top: 617px; background: var(--card-dark); }

  .plate-texture {
    position: absolute; inset: 0;
    background: radial-gradient(ellipse at 50% 35%, var(--plate-glow) 0%, var(--plate-mid) 40%, var(--plate-deep) 100%);
  }
  .front-wordmark {
    position: absolute;
    left: 0; right: 0; top: 150px;
    display: flex; align-items: center; justify-content: center; gap: 34px;
  }
  .wordmark-name {
    font-weight: 500;
    font-size: 150px;
    line-height: 1;
    letter-spacing: 10px;
    color: var(--steel);
  }
  .wordmark-ring {
    width: 120px; height: 120px;
    border: 8px solid var(--steel);
    border-radius: 50%;
  }

  .edge-band {
    position: absolute; left: 0; top: 0; bottom: 0;
    width: 38px;
    background: var(--brand-red);
  }
  .back-wordmark {
    position: absolute;
    left: 64px; top: 100px;
    display: flex; align-items: center; gap: 18px;
  }
  .back-wordmark .wordmark-name { font-size: 88px; letter-spacing: 6px; }
  .back-wordmark .wordmark-ring { width: 72px; height: 72px; border-width: 5px; }

  .service-list {
    position: absolute; left: 44px; top: 238px;
    list-style: none;
  }
  .service-list li {
    display: flex; align-items: center; gap: 6px;
    font-size: 23px; line-height: 38px;
    color: var(--text-light);
    text-transform: uppercase;
  }
  .service-list li::before {
    content: "";
    width: 21px; height: 21px;
    border-radius: 50%;
    background: var(--brand-red);
    border: 2px solid #cfcfcf;
  }
  .column-divider {
    position: absolute; left: 415px; top: 143px;
    width: 1px; height: 240px;
    background: var(--divider);
  }
  .contact-list {
    position: absolute; left: 437px; top: 146px;
    list-style: none;
  }
  .contact-list li {
    display: flex; align-items: flex-start; gap: 8px;
    font-size: 23px; line-height: 34px;
    color: var(--text-light);
    text-transform: uppercase;
  }
  .contact-icon { width: 22px; height: 22px; margin-top: 6px; flex: none; }
  .social-mark {
    width: 20px; height: 20px; margin: 7px 1px 0; flex: none;
    background: var(--accent-red); border-radius: 3px;
  }
  .contact-list .contact-website {
    font-size: 20px; line-height: 30px;
    color: var(--accent-red);
    margin-top: 8px;
    letter-spacing: 0.5px;
  }
</style>
</head>
<body>
  <section class="card card-front">
    <div class="plate-texture" role="img" aria-label="Dark red diamond-plate metal texture with a soft central glow"></div>
    <div class="front-wordmark">
      <span class="wordmark-name">KTV</span>
      <span class="wordmark-ring"></span>
    </div>
  </section>

  <section class="card card-back">
    <div class="edge-band"></div>
    <div class="back-wordmark">
      <span class="wordmark-name">KTV</span>
      <span class="wordmark-ring"></span>
    </div>
    <ul class="service-list">
      <li>Luxury Off Road Vehicle Sales</li>
      <li>Custom Off Road Bumpers</li>
    </ul>
    <div class="column-divider"></div>
    <ul class="contact-list">
      <li>
        <svg class="contact-icon" viewBox="0 0 24 24"><path fill="#a3262b" d="M12 1a8 8 0 0 0-8 8c0 6 8 14 8 14s8-8 8-14a8 8 0 0 0-8-8z"/><circle cx="12" cy="9" r="3" fill="#1c1a1a"/></svg>
        <span>518 Pelling Road, Suite 164.<br>Halvern Springs, Calder</span>
      </li>
      <li>
        <svg class="contact-icon" viewBox="0 0 24 24"><circle cx="12" cy="12" r="11" fill="#a3262b"/><path fill="#1c1a1a" d="M8 6l2.5 0 1 3-1.5 1.2a8 8 0 0 0 3.8 3.8L15 12.5l3 1V16a1.5 1.5 0 0 1-1.5 1.5A10.5 10.5 0 0 1 6.5 7.5 1.5 1.5 0 0 1 8 6z"/></svg>
        <span>555-318-0467</span>
      </li>
      <li><span class="social-mark"></span><span>KTVTRAILGEAR</span></li>
      <li><span class="social-mark"></span><span>KTV_TRAILGEAR</span></li>
      <li class="contact-website">WWW.KTV-TRAILGEAR.EXAMPLE</li>
    </ul>
  </section>
</body>
</html>
```